A layout of a webpage for oil trade platform

I would like to have a desgin of one page webpage (with section scrollling dowin) that woulf present the new product i.e. oil trade platform for wholesale buyers and sellers.
Layout should consist of the sections similar to the given at: https://strona.trawomirek.pl/modul-planowania-spotkan
However oil industy require more colors and more photo stories than here for doctor.
I. I woul imagine at first below menu a slider with brueg information about the product and its advantages with "more" button next to the prict screen of our platform on different displays (PC and mobile).
II. Bellow the slider I would imagine icons correspoing to the advantages of that plaftorm:
1. Purchase/sale process automation 24/7
2. Access to the best deals
3. Electronic offerings and orderings
4. Transaction status monitoring
5. Data and transaction security
II A) (optional):
In near future we would like to prepare a short video presenation. Hence please prepare a place to display that element here.
At the moment alternatvily please prepare a How it works section that would explan the platform operating process
III. Next secion is about benefits for Oil Purchaser
It can be done either by icons of by text and corresponding grahip for while section.
Benefits:
- Access to cheaper oil
- Convenience of online orders
- Possibility to compare prices on the market
- Transaction history
- Order status monitoring
- Seccurity and transparency of purchase
IV. Next seciont is about benefits for Oil Seller
Benefits:
- New sale channel
- Attracting new clients
- More oil sold
- Transaction security
- Possibility to integrate with distribution infrastructure and logistits for more efficient automation.
V. Contact form
VI. Footer
I would need a layout that that will correspond to the very dynamic logo but I would expect also a clean form, smoth and modern. It has to be proffessional layout with more corporate character.
It can use a paralax features if needed.
Attachments:
- logo design
- platfrom print screen
Industry/Entity Type
Oil And Gas
Number of Pages Required
1 page

```html
<!DOCTYPE html>
<html lang="en">
<head>
<meta charset="utf-8">
<title>Oilvane – Oil Trade Platform</title>
<link href="https://fonts.googleapis.com/css2?family=Montserrat:wght@400;600;700&family=Lato:ital,wght@0,400;0,700;1,400&family=Playfair+Display:ital@1&display=swap" rel="stylesheet">
<style>
:root{
  --orange:#f26522;
  --navy:#0f3260;
  --ink:#2b2f36;
  --text:#666a70;
  --dark:#353535;
  --darker:#2a2a2a;
  --deepest:#1f1f1f;
  --light:#f7f7f7;
  --field:#5a5a5a;
  --white:#ffffff;
}
*{margin:0;padding:0;box-sizing:border-box}
html,body{width:1200px;height:3905px;overflow:hidden}
body{font-family:'Lato',sans-serif;color:var(--text);background:var(--white);position:relative}
section,header,footer{position:absolute;left:0;width:1200px;overflow:hidden}
.abs{position:absolute}
.center{left:0;width:1200px;text-align:center}
.h-title{font-family:'Montserrat',sans-serif;font-weight:700;letter-spacing:1.5px;text-transform:uppercase}
.kicker{font-family:'Playfair Display',serif;font-style:italic;font-size:12px}
svg{display:block}

/* hero */
.hero{top:0;height:495px}
.hero-photo{position:absolute;inset:0;background:linear-gradient(180deg,#a9c3cb 0%,#8eaab3 45%,#5d7884 62%,#3e5663 100%)}
.nav{position:absolute;top:0;left:0;width:1200px;height:90px}
.brand{position:absolute;left:229px;top:28px;display:flex;align-items:center;gap:8px;font-family:'Montserrat',sans-serif;font-weight:700;font-size:19px;color:var(--navy)}
.brand-dot{width:20px;height:20px;border-radius:50%;background:var(--orange)}
.menu{position:absolute;left:554px;top:48px;display:flex;gap:26px;font-family:'Montserrat',sans-serif;font-size:9.5px;font-weight:700;color:var(--white);letter-spacing:.5px}
.menu .active{border-bottom:2px solid var(--orange);padding-bottom:4px}
.hero-title{left:281px;top:160px;font-family:'Montserrat',sans-serif;font-weight:700;font-size:33px;color:var(--white);letter-spacing:1px}
.hero-sub{left:300px;top:201px;font-size:13px;color:var(--white)}
.features{left:320px;top:222px;list-style:none;font-size:16px;color:var(--white);line-height:21px}
.features li::before{content:"";display:inline-block;width:7px;height:7px;background:var(--orange);margin-right:8px;vertical-align:middle}
.btn{display:inline-block;background:var(--orange);color:var(--white);font-family:'Montserrat',sans-serif;font-weight:700;font-size:9px;text-transform:uppercase;letter-spacing:1px;text-align:center}
.hero-btn{left:411px;top:320px;width:78px;height:26px;line-height:26px}
.dots{top:473px;left:575px;display:flex;gap:5px}
.dots span{width:9px;height:9px;border-radius:50%;background:var(--orange)}
.dots span.on{background:var(--white)}

/* advantages */
.advantages{top:495px;height:312px;background:var(--light)}
.adv-grid{position:absolute;top:140px;left:200px;width:800px;display:flex}
.adv-item{width:160px;text-align:center}
.adv-item svg{margin:0 auto 12px}
.adv-item h3{font-family:'Montserrat',sans-serif;font-size:7px;font-weight:700;color:var(--ink);text-transform:uppercase;margin-bottom:8px}
.adv-item p{font-size:7.5px;line-height:11px;padding:0 22px;color:#8a8d92}

/* video */
.video{top:807px;height:533px;background:var(--deepest)}
.video-photo{position:absolute;inset:0;background:radial-gradient(ellipse at 25% 30%,#4a4542 0%,#2a2828 45%,#1b1b1b 100%)}
.video-top{position:absolute;top:0;left:0;width:1200px;height:6px;background:#4a4a4a}
.video h2{top:160px;font-size:44px;color:var(--white)}
.play{position:absolute;left:561px;top:226px;width:78px;height:78px;border-radius:50%;background:var(--orange)}

/* how it works */
.how{top:1340px;height:396px;background:var(--navy)}
.how-photo{position:absolute;left:0;top:0;width:541px;height:396px;background:linear-gradient(135deg,#5e6a72 0%,#8b8f92 40%,#d9d6d2 60%,#e6783a 80%,#3b3f44 100%)}
.how-kick{left:580px;top:82px;font-family:'Montserrat',sans-serif;font-size:8px;font-weight:700;color:var(--orange);letter-spacing:1px;text-transform:uppercase}
.how h2{left:580px;top:96px;font-size:20px;color:var(--white)}
.how-desc{left:590px;top:124px;width:400px;font-size:9px;line-height:14px;color:#b9c4d4;font-style:italic}
.steps{left:581px;top:190px;display:grid;grid-template-columns:210px 210px;row-gap:18px}
.step{display:flex;align-items:center;gap:12px}
.step-ic{width:38px;height:38px;border-radius:50%;background:#2e3a4e;display:flex;align-items:center;justify-content:center}
.step small{display:block;font-size:7px;color:#b9c4d4}
.step b{font-family:'Montserrat',sans-serif;font-size:11px;color:var(--white);letter-spacing:.5px}
.how-btn{left:596px;top:310px;width:117px;height:30px;line-height:30px}

/* purchaser */
.purchaser{top:1736px;height:333px;background:var(--dark)}
.purchaser h2{top:19px;font-size:18px;color:var(--white)}
.pb-icon{position:absolute;top:79px;width:32px;height:32px;border-radius:50%;background:var(--white);display:flex;align-items:center;justify-content:center}
.pb-main{position:absolute;left:557px;top:100px;width:58px;height:58px;border-radius:50%;background:#d8d8d8;display:flex;align-items:center;justify-content:center}
.arrow{position:absolute;top:156px;width:26px;height:26px;border-radius:50%;display:flex;align-items:center;justify-content:center}
.arrow.left{left:266px;background:var(--white)}
.arrow.right{left:890px;border:1px solid var(--white)}
.pb-head{top:175px;font-family:'Montserrat',sans-serif;font-size:11px;font-weight:700;color:var(--orange)}
.pb-text{left:350px;top:210px;width:500px;text-align:center;font-style:italic;font-size:10px;line-height:15px;color:#e2e2e2}

/* sellers */
.sellers{top:2069px;height:417px;background:var(--white)}
.sellers h2{top:36px;font-size:20px;color:var(--navy)}
.sl-item{position:absolute;width:200px;text-align:center;font-size:13px;color:var(--ink)}
.sl-circle{width:72px;height:72px;margin:0 auto 14px;border:1.5px solid var(--orange);border-radius:50%;display:flex;align-items:center;justify-content:center}
.sl-wide{position:absolute;top:250px;left:0;width:1200px;text-align:center;font-size:13px;color:var(--ink)}
.sl-wide .sl-circle{margin-bottom:20px}

/* facts */
.facts{top:2486px;height:370px;background:var(--white)}
.facts .kicker{top:66px;color:#666}
.facts h2{top:86px;font-size:20px;color:var(--ink)}
.divider{position:absolute;left:560px;width:80px;height:1px;background:#cfcfcf}
.fact-row{position:absolute;top:174px;left:229px;display:flex;gap:18px}
.fact{width:169px;height:156px;background:#f3f3f3;text-align:center;padding-top:30px}
.fact svg{margin:0 auto 14px}
.fact b{display:block;font-family:'Montserrat',sans-serif;font-size:25px;color:var(--ink);margin-bottom:10px}
.fact small{font-size:8px;letter-spacing:1px;text-transform:uppercase;color:#777}

/* contact */
.contact{top:2856px;height:569px;background:var(--dark)}
.contact .kicker{top:60px;color:#ddd}
.contact h2{top:82px;font-size:24px;color:var(--white)}
.field{position:absolute;background:var(--field);color:#cfcfcf;font-size:8px;display:flex;align-items:center;gap:12px;padding-left:22px}
.field.area{align-items:flex-start;padding-top:14px}
.send{left:521px;top:473px;width:130px;height:31px;line-height:31px}

/* subscribe */
.subscribe{top:3425px;height:162px;background:var(--light)}
.sub-box{position:absolute;left:286px;top:63px;width:568px;height:42px;background:#ececec;display:flex}
.sub-box span{flex:1;padding-left:30px;line-height:42px;font-size:8px;color:#999}
.sub-btn{width:104px;height:42px;line-height:42px}

/* about */
.about{top:3587px;height:318px;background:var(--darker)}
.about .kicker{top:50px;color:var(--orange);font-size:15px}
.about h2{top:78px;font-size:19px;color:var(--white);letter-spacing:3px}
.about-text{left:380px;top:110px;width:440px;text-align:center;font-size:9.5px;line-height:15px;color:#cfcfcf;font-style:italic}
.socials{top:191px;left:482px;display:flex;gap:20px}
.socials span{width:25px;height:25px;border-radius:50%;background:#d8d8d8}
.copy{position:absolute;left:0;top:291px;width:1200px;height:27px;background:#202020;text-align:center;line-height:27px;font-size:8px;color:#cfcfcf}
</style>
</head>
<body>

<header class="hero">
  <div class="hero-photo" role="img" aria-label="Offshore oil platform standing in open sea under a pale sky"></div>
  <nav class="nav">
    <div class="brand"><span class="brand-dot"></span>Oilvane</div>
    <div class="menu">
      <span class="active">HOME</span><span>PRODUCT</span><span>ABOUT US</span><span>CONTACT US</span><span>SERVICES</span><span>TEAM</span>
      <svg width="11" height="11" viewBox="0 0 12 12"><path d="M1 2h2l1.5 6h6l1-4H4" fill="none" stroke="#fff" stroke-width="1.3"/><circle cx="5" cy="10.5" r="1" fill="#fff"/><circle cx="10" cy="10.5" r="1" fill="#fff"/></svg>
      <svg width="11" height="11" viewBox="0 0 12 12"><circle cx="5" cy="5" r="3.5" fill="none" stroke="#fff" stroke-width="1.4"/><path d="M7.5 7.5l3.5 3.5" stroke="#fff" stroke-width="1.4"/></svg>
    </div>
  </nav>
  <h1 class="abs hero-title">PRODUCT NAME</h1>
  <p class="abs hero-sub">Brief information about our oil trade platform</p>
  <ul class="abs features"><li>Feature 1</li><li>Feature 2</li><li>Feature 3</li></ul>
  <a class="abs btn hero-btn">See more</a>
  <div class="abs dots"><span></span><span></span><span class="on"></span><span></span><span></span></div>
</header>

<section class="advantages">
  <p class="abs center kicker" style="top:50px;color:#666">Who we are</p>
  <h2 class="abs center h-title" style="top:72px;font-size:21px;color:var(--ink)">Our Platform Advantages</h2>
  <svg class="abs" style="left:594px;top:108px" width="12" height="12" viewBox="0 0 12 12"><path d="M2 2l8 8M10 2l-8 8" stroke="#999" stroke-width="1.2"/></svg>
  <div class="adv-grid">
    <div class="adv-item">
      <svg width="22" height="22" viewBox="0 0 24 24"><circle cx="12" cy="12" r="9" fill="none" stroke="#f26522" stroke-width="1.5"/><path d="M12 7v5l3 2" fill="none" stroke="#f26522" stroke-width="1.5"/></svg>
      <h3>Purchase/sale process automation 24/7</h3><p>Orders and sales run on their own, day and night</p>
    </div>
    <div class="adv-item">
      <svg width="22" height="22" viewBox="0 0 24 24"><path d="M6 18V10a6 6 0 0 1 12 0v8M4 18h16" fill="none" stroke="#f26522" stroke-width="1.5"/></svg>
      <h3>Access to the best deals</h3><p>See the best market offers from trusted sellers</p>
    </div>
    <div class="adv-item">
      <svg width="22" height="22" viewBox="0 0 24 24"><rect x="6" y="3" width="12" height="18" rx="1" fill="none" stroke="#f26522" stroke-width="1.5"/><path d="M9 8h6M9 12h6M9 16h4" stroke="#f26522" stroke-width="1.5"/></svg>
      <h3>Electronic offerings and orderings</h3><p>Send offers and place orders fully online</p>
    </div>
    <div class="adv-item">
      <svg width="22" height="22" viewBox="0 0 24 24"><rect x="3" y="5" width="18" height="12" rx="1" fill="none" stroke="#f26522" stroke-width="1.5"/><path d="M9 20h6M12 17v3" stroke="#f26522" stroke-width="1.5"/></svg>
      <h3>Transaction status monitoring</h3><p>Follow every deal step by step in real time</p>
    </div>
    <div class="adv-item">
      <svg width="22" height="22" viewBox="0 0 24 24"><path d="M12 3l7 3v6c0 4-3 7-7 9-4-2-7-5-7-9V6z" fill="none" stroke="#f26522" stroke-width="1.5"/><path d="M9 12l2 2 4-4" fill="none" stroke="#f26522" stroke-width="1.5"/></svg>
      <h3>Data and transaction security</h3><p>Your data and payments stay safe and private</p>
    </div>
  </div>
</section>

<section class="video">
  <div class="video-photo" role="img" aria-label="Portrait photo of a bearded man in glasses and a beanie against a dark background"></div>
  <div class="video-top"></div>
  <h2 class="abs center h-title">Watch Our Video</h2>
  <div class="play"><svg width="78" height="78" viewBox="0 0 78 78"><path d="M32 26l20 13-20 13z" fill="#fff"/></svg></div>
</section>

<section class="how">
  <div class="how-photo" role="img" aria-label="Hand holding an orange fuel pump nozzle"></div>
  <p class="abs how-kick">Check &amp; Guide</p>
  <h2 class="abs h-title how-h" style="left:580px;top:96px;font-size:20px;color:var(--white)">How It's Work</h2>
  <p class="abs how-desc">Description about How it's work onClick Description about How it's work onClick Description about How it's work onClick Description about How it's work onClick Description about How it's work onClick Description about How it's work onClick</p>
  <div class="abs steps">
    <div class="step"><span class="step-ic"><svg width="16" height="16" viewBox="0 0 16 16"><rect x="3" y="3" width="10" height="10" fill="none" stroke="#fff" stroke-width="1.3"/></svg></span><div><small>Step 1</small><b>Extensive Pack</b></div></div>
    <div class="step"><span class="step-ic"><svg width="16" height="16" viewBox="0 0 16 16"><rect x="4" y="2" width="8" height="12" fill="none" stroke="#fff" stroke-width="1.3"/></svg></span><div><small>Step 2</small><b>Extensive Pack</b></div></div>
    <div class="step"><span class="step-ic"><svg width="16" height="16" viewBox="0 0 16 16"><path d="M3 13L13 3M9 3h4v4" fill="none" stroke="#fff" stroke-width="1.3"/></svg></span><div><small>Step 3</small><b>Extensive Pack</b></div></div>
    <div class="step"><span class="step-ic"><svg width="16" height="16" viewBox="0 0 16 16"><circle cx="8" cy="8" r="5" fill="none" stroke="#fff" stroke-width="1.3"/></svg></span><div><small>Step 4</small><b>Extensive Pack</b></div></div>
  </div>
  <a class="abs btn how-btn">▷ Play video</a>
</section>

<section class="purchaser">
  <h2 class="abs center h-title">Benefits for Oil Purchaser</h2>
  <div class="pb-icon" style="left:445px"><svg width="14" height="14" viewBox="0 0 16 16"><rect x="2" y="4" width="12" height="9" fill="none" stroke="#f26522" stroke-width="1.4"/></svg></div>
  <div class="pb-icon" style="left:505px"><svg width="14" height="14" viewBox="0 0 16 16"><circle cx="8" cy="8" r="6" fill="none" stroke="#f26522" stroke-width="1.4"/><path d="M2 8h12M8 2v12" stroke="#f26522" stroke-width="1.2"/></svg></div>
  <div class="pb-main"><svg width="22" height="22" viewBox="0 0 24 24"><rect x="5" y="4" width="14" height="16" fill="none" stroke="#f26522" stroke-width="1.6"/><path d="M9 9h6M9 13h6" stroke="#f26522" stroke-width="1.6"/></svg></div>
  <div class="pb-icon" style="left:637px"><svg width="14" height="14" viewBox="0 0 16 16"><rect x="3" y="2" width="10" height="12" fill="none" stroke="#f26522" stroke-width="1.4"/><path d="M6 6h4M6 9h4" stroke="#f26522" stroke-width="1.2"/></svg></div>
  <div class="pb-icon" style="left:695px"><svg width="14" height="14" viewBox="0 0 16 16"><rect x="2" y="3" width="12" height="8" fill="none" stroke="#f26522" stroke-width="1.4"/><path d="M6 14h4" stroke="#f26522" stroke-width="1.4"/></svg></div>
  <div class="pb-icon" style="left:755px"><svg width="14" height="14" viewBox="0 0 16 16"><path d="M4 14V2h6l-2 3 2 3H4" fill="none" stroke="#f26522" stroke-width="1.4"/></svg></div>
  <div class="arrow left"><svg width="10" height="10" viewBox="0 0 10 10"><path d="M6 2L3 5l3 3" fill="none" stroke="#333" stroke-width="1.5"/></svg></div>
  <div class="arrow right"><svg width="10" height="10" viewBox="0 0 10 10"><path d="M4 2l3 3-3 3" fill="none" stroke="#fff" stroke-width="1.5"/></svg></div>
  <p class="abs center pb-head">Possibility to compare prices on the market</p>
  <p class="abs pb-text">Lorem ipsum dolor sit amet, consectetur adipiscing elit. Vestibulum egestas lacus pretium rhoncus a quis nisly tilt vehicula gravida dui in pulvinar donec diam elit consequat eget augue vitae aliquet sollicitudin.</p>
</section>

<section class="sellers">
  <h2 class="abs center h-title">Benefits for Oil Sellers</h2>
  <div class="sl-item" style="left:215px;top:120px"><div class="sl-circle"><svg width="24" height="24" viewBox="0 0 24 24"><path d="M5 18h14M8 18v-5h8v5M12 13V6" fill="none" stroke="#f26522" stroke-width="1.5"/></svg></div>New sale channel</div>
  <div class="sl-item" style="left:402px;top:120px"><div class="sl-circle"><svg width="24" height="24" viewBox="0 0 24 24"><circle cx="9" cy="9" r="3" fill="none" stroke="#f26522" stroke-width="1.5"/><circle cx="16" cy="10" r="2.5" fill="none" stroke="#f26522" stroke-width="1.5"/><path d="M3 19c1-4 4-5 6-5s5 1 6 5" fill="none" stroke="#f26522" stroke-width="1.5"/></svg></div>Attracting new clients</div>
  <div class="sl-item" style="left:585px;top:120px"><div class="sl-circle"><svg width="24" height="24" viewBox="0 0 24 24"><path d="M3 5h3l2 9h10l2-6H7" fill="none" stroke="#f26522" stroke-width="1.5"/><circle cx="9" cy="18" r="1.3" fill="#f26522"/><circle cx="17" cy="18" r="1.3" fill="#f26522"/></svg></div>More oil sold</div>
  <div class="sl-item" style="left:775px;top:120px"><div class="sl-circle"><svg width="24" height="24" viewBox="0 0 24 24"><rect x="6" y="5" width="12" height="15" fill="none" stroke="#f26522" stroke-width="1.5"/><path d="M9 10h6M9 14h6" stroke="#f26522" stroke-width="1.5"/></svg></div>Transaction security</div>
  <div class="sl-wide"><div class="sl-circle"><svg width="24" height="24" viewBox="0 0 24 24"><circle cx="7" cy="17" r="1.5" fill="#f26522"/><path d="M6 11a7 7 0 0 1 7 7M6 6a12 12 0 0 1 12 12" fill="none" stroke="#f26522" stroke-width="1.5"/></svg></div>Possibility to integrate with distribution infrastructure and logistits for more efficient automation.</div>
</section>

<section class="facts">
  <p class="abs center kicker">Consectetur Adipiscing</p>
  <h2 class="abs center h-title">Our Fun Facts</h2>
  <div class="divider" style="top:133px"></div>
  <div class="fact-row">
    <div class="fact"><svg width="16" height="18" viewBox="0 0 16 18"><rect x="2" y="1" width="12" height="16" fill="none" stroke="#555" stroke-width="1.4"/><path d="M5 6h6M5 10h6" stroke="#555" stroke-width="1.4"/></svg><b>159</b><small>Member</small></div>
    <div class="fact"><svg width="16" height="18" viewBox="0 0 16 18"><rect x="2" y="1" width="12" height="16" fill="none" stroke="#555" stroke-width="1.4"/><path d="M5 6h6M5 10h6" stroke="#555" stroke-width="1.4"/></svg><b>1,394</b><small>Happy clients</small></div>
    <div class="fact"><svg width="16" height="18" viewBox="0 0 16 18"><rect x="2" y="1" width="12" height="16" fill="none" stroke="#555" stroke-width="1.4"/><path d="M5 6h6M5 10h6" stroke="#555" stroke-width="1.4"/></svg><b>1,834</b><small>Oil sellers</small></div>
    <div class="fact"><svg width="16" height="18" viewBox="0 0 16 18"><rect x="2" y="1" width="12" height="16" fill="none" stroke="#555" stroke-width="1.4"/><path d="M5 6h6M5 10h6" stroke="#555" stroke-width="1.4"/></svg><b>134</b><small>Collaborations</small></div>
  </div>
</section>

<section class="contact">
  <p class="abs center kicker">Consectetur Adipiscing</p>
  <h2 class="abs center h-title">Leave a Message Box</h2>
  <div class="field" style="left:229px;top:153px;width:357px;height:37px"><svg width="10" height="10" viewBox="0 0 10 10"><circle cx="5" cy="3" r="2" fill="#ccc"/><path d="M1 10c0-3 2-4 4-4s4 1 4 4" fill="#ccc"/></svg>Name *</div>
  <div class="field" style="left:604px;top:153px;width:357px;height:37px"><svg width="10" height="10" viewBox="0 0 10 10"><rect x="1" y="2" width="8" height="6" fill="#ccc"/></svg>Email *</div>
  <div class="field" style="left:229px;top:208px;width:732px;height:34px"><svg width="10" height="10" viewBox="0 0 10 10"><circle cx="5" cy="5" r="4" fill="#ccc"/></svg>Website *</div>
  <div class="field area" style="left:229px;top:257px;width:732px;height:172px">Write Comment</div>
  <a class="abs btn send">Send</a>
</section>

<section class="subscribe">
  <div class="sub-box"><span>Enter your email</span><a class="btn sub-btn">Subscribe ➤</a></div>
</section>

<footer class="about">
  <p class="abs center kicker">About us</p>
  <h2 class="abs center h-title">About Oilvane</h2>
  <p class="abs about-text">About us write something about us About us write something about us About us write something about us About us write something about us About us write something about us About us write something about us About us write something about us.</p>
  <div class="abs socials"><span></span><span></span><span></span><span></span><span></span></div>
  <div class="copy">© Copyright Oilvane 2017 · All Rights Reserved</div>
</footer>

</body>
</html>
```